Banner/Sign artwork for sign shop

We're after a clean, modern almost minimalist sign design for across the front of our new shop. Size is approximately 5.3m wide x 3m high.
We're a small sign & print shop looking to attract larger corporate customers. Sign to consist of our contact details, maybe a slogan? and some icons of products we supply. Ie: a-frames, banners, flags, vehicle signage etc etc. Our colours are orange, black and white. Would really like a catchy graphic or similar for passers by to notice as there is a lot of traffic during the day.
Please not a busy or crowded design.
Will be carrying this style through on additional signage, cards, flyers etc.
Horizontal and stacked NEW logo attached.
Photo of where this sign is to go. Awning will already have our logo... new sign to go underneath where the pink section is (and carried around the side).

Looking forward to working with you!

• Our contact details - phone, website and KD logo
Clean professional look to show we're not an unprofessional backyard type of shop
We are on a main road, so the layout can't be "busy". must be easy to read.

PLEASE READ DESCRIPTION
• Icons for products?
Would be great to have a graphic, or set of graphics we can use on future signage and advertising. We have pixelvaultz account, so feel free to grab anything from there and we can then download the high res file.
• Logo DOESN'T need to appear on banner, as it's on shop awning above!
Can't be too busy with information.
Can't have really small text

```html
<!DOCTYPE html>
<html lang="en">
<head>
<meta charset="utf-8">
<title>Sign Shop Storefront Banner</title>
<link rel="stylesheet" href="https://fonts.googleapis.com/css2?family=Lato:wght@700;900&display=swap">
<style>
  :root {
    --orange: #e3691c;
    --orange-tint: #f6d2ba;
    --black: #0c0c0c;
    --white: #ffffff;
    --sky: #c3d3ea;
    --backdrop: #e9e9e7;
  }
  html, body {
    margin: 0;
    padding: 0;
    width: 1200px;
    height: 801px;
    overflow: hidden;
    background: var(--backdrop);
  }
  .canvas {
    position: relative;
    width: 1200px;
    height: 801px;
  }
  .banner {
    position: absolute;
    left: 20px;
    top: 128px;
    width: 1160px;
    height: 545px;
    box-shadow: 0 4px 18px rgba(0,0,0,0.12);
  }
  .product-label {
    font-family: "Lato", sans-serif;
    font-weight: 900;
    font-size: 39px;
    fill: var(--black);
  }
  .contact-text {
    font-family: "Lato", sans-serif;
    font-weight: 900;
    font-size: 34px;
    fill: var(--black);
  }
  .timeline { fill: none; stroke: var(--black); stroke-width: 4; }
  .icon-line { fill: none; stroke: var(--white); stroke-width: 4; stroke-linejoin: round; stroke-linecap: round; }
  .accent-dot { fill: var(--orange); }
  .accent-tint { fill: var(--orange-tint); }
</style>
</head>
<body>
<main class="canvas">
  <svg class="banner" viewBox="0 0 1680 790" xmlns="http://www.w3.org/2000/svg" aria-label="Sign shop banner listing frames, banners, flags and vehicle signage">
    <defs>
      <linearGradient id="corner-top" x1="0" y1="0" x2="1" y2="1">
        <stop offset="0" stop-color="var(--orange)"/>
        <stop offset="0.55" stop-color="var(--orange)" stop-opacity="0.55"/>
        <stop offset="1" stop-color="var(--sky)" stop-opacity="0"/>
      </linearGradient>
      <linearGradient id="corner-bottom" x1="0" y1="0" x2="1" y2="1">
        <stop offset="0" stop-color="var(--sky)" stop-opacity="0"/>
        <stop offset="0.45" stop-color="var(--orange)" stop-opacity="0.55"/>
        <stop offset="1" stop-color="var(--orange)"/>
      </linearGradient>
    </defs>

    <rect class="banner-field" width="1680" height="790" fill="var(--white)"/>

    <!-- corner colour fields -->
    <rect class="corner-field" x="0" y="0" width="760" height="190" fill="url(#corner-top)" role="img" aria-label="Flowing orange and pale blue wave decoration in the top left corner"/>
    <rect class="corner-field" x="700" y="600" width="980" height="190" fill="url(#corner-bottom)" role="img" aria-label="Flowing orange and pale blue wave decoration along the bottom right"/>

    <!-- accent tints where dot textures sit -->
    <rect class="accent-tint" x="1338" y="14" width="210" height="42" opacity="0.6" role="img" aria-label="Orange dot texture"/>
    <rect class="accent-tint" x="22" y="282" width="50" height="68" opacity="0.6" role="img" aria-label="Orange dot texture"/>
    <rect class="accent-tint" x="1518" y="205" width="40" height="260" opacity="0.6" role="img" aria-label="Orange dot texture"/>
    <circle class="accent-dot" cx="65" cy="445" r="12"/>
    <circle cx="1171" cy="50" r="12" fill="none" stroke="var(--black)" stroke-width="2.5"/>

    <!-- product timeline -->
    <path class="timeline" d="M202,328 H277 A125,125 0 0 1 527,328 H572 A125,125 0 0 0 822,328 H865 A125,125 0 0 1 1115,328 H1158 A125,125 0 0 0 1408,328 H1472"/>
    <circle cx="202" cy="328" r="8" fill="var(--black)"/>
    <circle cx="1472" cy="328" r="8" fill="var(--black)"/>

    <g class="product product-frames">
      <circle cx="402" cy="328" r="102" fill="var(--orange)"/>
      <g class="icon-line">
        <rect x="362" y="308" width="80" height="58"/>
        <rect x="372" y="318" width="60" height="38"/>
        <path d="M362,308 L402,290 L442,308"/>
        <circle cx="402" cy="290" r="5"/>
      </g>
    </g>

    <g class="product product-banners">
      <circle cx="697" cy="328" r="102" fill="var(--black)"/>
      <g class="icon-line">
        <rect x="657" y="298" width="80" height="44"/>
        <path d="M662,288 H732 M670,288 V298 M724,288 V298"/>
        <path d="M657,352 H737 M675,342 V366 M719,342 V366 M665,366 H685 M709,366 H729"/>
      </g>
    </g>

    <g class="product product-flags">
      <circle cx="990" cy="328" r="102" fill="var(--orange)"/>
      <g class="icon-line">
        <path d="M957,288 V370"/>
        <path d="M957,294 H990 V306 H1024 L1014,322 L1024,338 H985 V326 H957"/>
      </g>
    </g>

    <g class="product product-vehicle">
      <circle cx="1280" cy="328" r="102" fill="var(--black)"/>
      <g class="icon-line">
        <path d="M1235,298 H1295 V348 H1235 Z"/>
        <path d="M1295,318 H1312 L1325,334 V348 H1295"/>
        <circle cx="1254" cy="352" r="8"/>
        <circle cx="1310" cy="352" r="8"/>
        <path d="M1244,336 L1258,320 L1268,330 L1276,322 L1288,336"/>
        <circle cx="1250" cy="308" r="3"/>
      </g>
    </g>

    <text class="product-label" x="400" y="498" text-anchor="middle">Frames</text>
    <text class="product-label" x="703" y="497" text-anchor="middle">Banners</text>
    <text class="product-label" x="992" y="497" text-anchor="middle">Flags</text>
    <text class="product-label" x="1285" y="495" text-anchor="middle">Vehicle Signage</text>

    <!-- contact details -->
    <g class="contact contact-phone">
      <circle cx="93" cy="645" r="27" fill="var(--orange)"/>
      <path d="M82,632 C80,648 92,660 106,658 L108,650 L100,646 L96,650 C91,648 88,644 86,640 L90,636 L87,628 Z" fill="var(--white)"/>
      <text class="contact-text" x="137" y="657">012 345 6789</text>
    </g>
    <g class="contact contact-web">
      <circle cx="92" cy="718" r="27" fill="var(--orange)"/>
      <g fill="none" stroke="var(--white)" stroke-width="2.5">
        <circle cx="92" cy="718" r="14"/>
        <ellipse cx="92" cy="718" rx="6" ry="14"/>
        <path d="M78,718 H106 M81,710 H103 M81,726 H103"/>
      </g>
      <text class="contact-text" x="135" y="730">www.signmarkly.com</text>
    </g>
  </svg>
</main>
</body>
</html>
```